Business Card Design Needed

Business car design required, logo will be supplied.

Brackenfield Heat Surveyors are looking to become the leading provider of energy performance certificates to estate agents, landlords and home owners in the Yorkshire region of the UK.

The business card must be double sided and professional looking. Estate agents receive hundreds of cards from contractors and our card must stand out.

I require a two sided business card that is clean, modern and created by a designer that can think outside of the box.

Brand colours can be supplied .

Please ask if you have any questions.

Target Market(s)

Estate agents, landlords and property owners

Industry/Entity Type

Property - estate agency - energy consultants

Contact Information for Business Card

Tomas Birchwell - Energy Assessor - 07351642170 - www.BrackenfieldHSV.co.uk - info@brackenfieldhsv.co.uk

Font styles to use
Serif
Sans Serif

Colors
00AB8E
00BBA5
67D7C9
C6EFE9
E9F9F6

Requirements
Must have
• Use the provided logo, clean, professional and stand out from the crowd
Nice to have
• Clever use of text, spacing and brand colours
Should not have
• Clip art

```html
<!DOCTYPE html>
<html lang="en">
<head>
<meta charset="utf-8">
<title>Brackenfield Heat Surveyors – Business Card</title>
<link rel="stylesheet" href="https://fonts.googleapis.com/css2?family=Questrial&display=swap">
<style>
  :root {
    --brand-blue: #0062a0;
    --brand-lime: #a9c400;
    --card-white: #ffffff;
    --stage-grey: #e6e6e6;
    --divider-blue: #2f86c8;
  }
  * { box-sizing: border-box; margin: 0; padding: 0; }
  html, body {
    width: 1200px;
    height: 900px;
    overflow: hidden;
  }
  body {
    background: var(--stage-grey);
    font-family: "Questrial", "Century Gothic", sans-serif;
    position: relative;
  }
  .card {
    position: absolute;
    left: 250px;
    width: 700px;
    height: 400px;
    overflow: hidden;
    box-shadow: 0 2px 6px rgba(0,0,0,0.12);
  }

  /* Front side */
  .card-front {
    top: 470px;
    background: var(--brand-lime);
  }
  .front-band {
    position: absolute;
    left: 0; top: 0;
    width: 44px; height: 100%;
    background: var(--brand-blue);
  }
  .front-stripe {
    position: absolute;
    left: 44px; top: 0;
    width: 6px; height: 100%;
    background: var(--card-white);
  }
  .front-mark {
    position: absolute;
    left: 140px; top: 160px;
    width: 80px; height: 80px;
    border-radius: 50%;
    background: var(--brand-blue);
  }
  .front-divider {
    position: absolute;
    left: 252px; top: 160px;
    width: 2px; height: 82px;
    background: var(--brand-blue);
  }
  .front-name {
    position: absolute;
    left: 274px; top: 166px;
    color: var(--brand-blue);
    font-weight: 400;
  }
  .front-name .name-main {
    display: block;
    font-size: 40px;
    line-height: 1;
    letter-spacing: 1px;
  }
  .front-name .name-sub {
    display: block;
    margin-top: 16px;
    font-size: 14px;
    letter-spacing: 0.55em;
  }

  /* Back side */
  .card-back {
    top: 40px;
    background: var(--card-white);
  }
  .back-brand {
    position: absolute;
    left: 40px; top: 90px;
    width: 220px;
    text-align: center;
  }
  .back-mark {
    width: 86px; height: 86px;
    margin: 0 auto 14px;
    border-radius: 50%;
    background: var(--brand-lime);
  }
  .back-brand-name {
    color: var(--brand-blue);
    font-size: 15px;
    letter-spacing: 0.08em;
    text-transform: uppercase;
    line-height: 1.4;
  }
  .back-divider {
    position: absolute;
    left: 292px; top: 60px;
    width: 2px; height: 280px;
    background: var(--divider-blue);
  }
  .back-details {
    position: absolute;
    left: 330px; top: 96px;
  }
  .person-name {
    color: var(--brand-blue);
    font-size: 34px;
    line-height: 1.1;
  }
  .person-role {
    color: var(--brand-lime);
    font-size: 13px;
    letter-spacing: 0.3em;
    margin-top: 4px;
    text-transform: uppercase;
  }
  .contact-list {
    list-style: none;
    margin-top: 34px;
  }
  .contact-item {
    display: flex;
    align-items: center;
    gap: 12px;
    color: var(--brand-blue);
    font-size: 18px;
    line-height: 1;
    margin-bottom: 14px;
  }
  .contact-icon {
    width: 20px; height: 20px;
    flex: none;
  }
</style>
</head>
<body>

  <section class="card card-back" aria-label="Business card, contact side">
    <div class="back-brand">
      <div class="back-mark"></div>
      <p class="back-brand-name">Brackenfield<br>Heat Surveyors</p>
    </div>
    <div class="back-divider"></div>
    <div class="back-details">
      <h1 class="person-name">Tomas Birchwell</h1>
      <p class="person-role">Energy Assessor</p>
      <ul class="contact-list">
        <li class="contact-item">
          <svg class="contact-icon" viewBox="0 0 20 20" aria-hidden="true">
            <path d="M6 2 C4 3 3 5 4 8 C5 12 8 15 12 16 C15 17 17 16 18 14 L15 11 L13 13 C10 12 8 10 7 7 L9 5 Z" fill="var(--brand-lime)"/>
          </svg>
          <span>07351642170</span>
        </li>
        <li class="contact-item">
          <svg class="contact-icon" viewBox="0 0 20 20" aria-hidden="true">
            <g fill="none" stroke="var(--brand-lime)" stroke-width="1.6">
              <circle cx="10" cy="10" r="8"/>
              <ellipse cx="10" cy="10" rx="3.5" ry="8"/>
              <line x1="2" y1="10" x2="18" y2="10"/>
              <line x1="3.5" y1="6" x2="16.5" y2="6"/>
              <line x1="3.5" y1="14" x2="16.5" y2="14"/>
            </g>
          </svg>
          <span>www.BrackenfieldHSV.co.uk</span>
        </li>
        <li class="contact-item">
          <svg class="contact-icon" viewBox="0 0 20 20" aria-hidden="true">
            <rect x="1" y="4" width="18" height="12" fill="var(--brand-lime)"/>
            <path d="M1 4 L10 11 L19 4" fill="none" stroke="var(--card-white)" stroke-width="1.4"/>
          </svg>
          <span>info@brackenfieldhsv.co.uk</span>
        </li>
      </ul>
    </div>
  </section>

  <section class="card card-front" aria-label="Business card, brand side">
    <div class="front-band"></div>
    <div class="front-stripe"></div>
    <div class="front-mark"></div>
    <div class="front-divider"></div>
    <p class="front-name">
      <span class="name-main">BRACKENFIELD</span>
      <span class="name-sub">HEAT SURVEYORS</span>
    </p>
  </section>

</body>
</html>
```